Medical group practice

We need a flyer design incorporating the three doctors in the practice, there is a general practitioner, ophthalmologist and an obstetrician & Gynaecologist. see the attached file for the concept. will leave the colour design up to you

Target Market(s)

general public

Industry/Entity Type

Health Care

Colors

Designer to choose colors to be used in the design.

Requirements
Must have
• logos included in attachement

```html
<!DOCTYPE html>
<html lang="en">
<head>
<meta charset="utf-8">
<title>Northgate Medical – Flyer</title>
<link href="https://fonts.googleapis.com/css2?family=Open+Sans:wght@300;400;600;700&display=swap" rel="stylesheet">
<style>
:root{
  --red:#e3242b;
  --red-deep:#c8121c;
  --red-ring:#f2a3a8;
  --grey-band:#6d6d6d;
  --ink:#222;
  --grey-text:#666;
  --line:#d9d9d9;
  --white:#fff;
  --stage:#ececec;
}
*{box-sizing:border-box;margin:0;padding:0}
html,body{width:900px;height:1200px;overflow:hidden;background:var(--stage);font-family:"Open Sans",Arial,sans-serif}
.flyer{position:absolute;left:34px;top:13px;width:640px;height:903px;background:var(--white);transform:scale(1.3);transform-origin:top left;overflow:hidden}
.abs{position:absolute}
.brand{left:20px;top:70px;width:230px;text-align:center}
.brand-mark{width:60px;height:60px;border-radius:50%;background:var(--red);margin:0 auto 18px}
.brand-name{font-weight:700;font-size:16px;letter-spacing:1px;color:var(--ink)}
.team-photo{left:255px;top:0;width:385px;height:258px;background:linear-gradient(180deg,#ffffff 0%,#eef3f7 60%,#dfe8ef 100%)}
.hours-band{left:0;top:258px;width:640px;height:64px;background:var(--grey-band);color:var(--white)}
.hours-title{left:28px;top:8px;font-size:36px;font-weight:600;white-space:nowrap}
.hours-times{left:337px;top:8px;font-size:18.5px;font-weight:600;line-height:25px}
.tagline{left:0;top:334px;width:640px;text-align:center;font-size:34px;font-weight:300;color:var(--ink);letter-spacing:.3px}
.tagline em{font-style:normal;color:var(--red)}
.tagline-rule{left:0;top:382px;width:640px;height:1px;background:var(--red)}
.col{top:0;height:903px}
.col-gp{left:0;width:215px}
.col-eye{left:217px;width:204px}
.col-ob{left:423px;width:217px}
.col-head{position:absolute;top:396px;left:0;width:100%;text-align:center}
.specialty{font-size:12.5px;font-weight:600;color:var(--red)}
.phone{font-size:12.5px;font-weight:600;color:var(--ink);margin-top:6px}
.col-panel{position:absolute;top:492px;left:0;width:100%;height:341px;background:var(--red)}
.col-eye .col-panel{background:var(--red-deep);height:356px}
.col-divider{position:absolute;top:395px;width:1px;height:97px;background:var(--line)}
.badge{position:absolute;top:445px;left:50%;margin-left:-60px;width:120px;height:120px;border-radius:50%;background:var(--red-ring);display:flex;align-items:center;justify-content:center}
.badge-inner{width:100px;height:100px;border-radius:50%;background:var(--white);display:flex;align-items:center;justify-content:center;text-align:center}
.badge-art{width:74px;height:60px;border-radius:8px;background:linear-gradient(135deg,#e6f1f6,#cfe3ec)}
.badge-art.ob{background:linear-gradient(135deg,#e4ebf4,#dbeedd)}
.badge-name{font-size:10px;font-weight:600;color:var(--red-deep);line-height:13px;width:80px}
.doctor{position:absolute;top:585px;left:18px;right:8px;color:var(--white)}
.doctor-name{font-size:14.5px;font-weight:700}
.doctor-role{font-size:11.5px;line-height:14px}
.col-ob .doctor-role{font-size:10.5px}
.email{position:absolute;top:633px;left:18px;display:flex;align-items:center;gap:6px;font-size:11px;font-weight:600;color:var(--white);white-space:nowrap}
.email svg{flex:none}
.panel-rule{position:absolute;top:662px;left:0;width:100%;height:1px;background:rgba(255,255,255,.45)}
.services{position:absolute;top:679px;left:16px;right:6px;list-style:none;color:var(--white);font-size:11px;line-height:17px}
.services li{padding-left:10px;position:relative}
.services li::before{content:"";position:absolute;left:0;top:7px;width:4px;height:4px;border-radius:50%;background:var(--white)}
.services-group{font-size:10.8px;line-height:14.7px}
.services-group li{margin-bottom:10px}
.services-group li::before{top:6px;width:5px;height:5px}
.services-group strong{display:block;font-size:12px;font-weight:700;margin-bottom:2px}
.footer{left:0;top:860px;width:640px;height:43px}
.address{left:16px;top:8px;display:flex;align-items:center;gap:8px;font-size:15px;color:var(--grey-text)}
.footer-divider{left:320px;top:6px;width:1px;height:32px;background:var(--line)}
.footer-phone{left:336px;top:3px;display:flex;align-items:center;gap:8px;font-size:23px;font-weight:600;color:var(--grey-text);white-space:nowrap}
</style>
</head>
<body>
<main class="flyer">
  <header>
    <div class="abs brand">
      <div class="brand-mark"></div>
      <div class="brand-name">NORTHGATE MEDICAL</div>
    </div>
    <div class="abs team-photo" role="img" aria-label="Photo of smiling medical team in white coats giving thumbs up"></div>
  </header>

  <section class="abs hours-band">
    <div class="abs hours-title">Opening hours :</div>
    <div class="abs hours-times">Monday – Fridays 9am-6pm,<br>Saturdays 10am – 5pm</div>
  </section>

  <h1 class="abs tagline">YOUR <em>HEALTH</em> IS OUR PRIORITY</h1>
  <div class="abs tagline-rule"></div>

  <section class="abs col col-gp">
    <div class="col-head">
      <div class="specialty">General Practitioner -</div>
      <div class="phone">(555) 014 2281</div>
    </div>
    <div class="col-panel"></div>
    <div class="badge"><div class="badge-inner"><div class="badge-art" role="img" aria-label="General practice emblem"></div></div></div>
    <div class="doctor">
      <div class="doctor-name">Dr. Lionel Ashby, MD.</div>
      <div class="doctor-role">General Practitioner</div>
    </div>
    <div class="email">
      <svg width="15" height="15" viewBox="0 0 16 16"><circle cx="8" cy="8" r="8" fill="#fff"/><rect x="4" y="5" width="8" height="6" fill="none" stroke="#e3242b" stroke-width="1.2"/><path d="M4 5l4 3.5L12 5" fill="none" stroke="#e3242b" stroke-width="1.2"/></svg>
      lionel.ashby.doc@mailbox.com
    </div>
    <div class="panel-rule"></div>
    <ul class="services">
      <li>General Checks</li>
      <li>Annual Check ups</li>
      <li>Wound Care/Dressings</li>
      <li>Incision &amp; Drainage</li>
      <li>Suturing lacerations</li>
      <li>Pain Injections</li>
      <li>Glucose checks</li>
      <li>Foreign Body Removal</li>
    </ul>
  </section>

  <section class="abs col col-eye">
    <div class="col-divider" style="left:-1px"></div>
    <div class="col-head">
      <div class="specialty">Ophthalmologist -</div>
      <div class="phone">(555) 014 7730</div>
    </div>
    <div class="col-panel"></div>
    <div class="badge"><div class="badge-inner"><div class="badge-name">Clearview Eye Care</div></div></div>
    <div class="doctor">
      <div class="doctor-name">Dr. Teresa M. Valdez</div>
      <div class="doctor-role">MD. Surgeon Ophthalmologist</div>
    </div>
    <div class="email">
      <svg width="15" height="15" viewBox="0 0 16 16"><circle cx="8" cy="8" r="8" fill="#fff"/><rect x="4" y="5" width="8" height="6" fill="none" stroke="#c8121c" stroke-width="1.2"/><path d="M4 5l4 3.5L12 5" fill="none" stroke="#c8121c" stroke-width="1.2"/></svg>
      t.valdez.eye@mailbox.com
    </div>
    <div class="panel-rule"></div>
    <ul class="services">
      <li>Eyes disease examination</li>
      <li>Surgery of Pterygium</li>
      <li>Cataract</li>
      <li>Glaucoma</li>
      <li>Emergency: Conjunctivitis</li>
      <li>Traumatism</li>
      <li>Foreign body and more</li>
    </ul>
    <div class="col-divider" style="left:204px"></div>
  </section>

  <section class="abs col col-ob">
    <div class="col-head">
      <div class="specialty">Obstetrician/Gynaecologist –</div>
      <div class="phone">(555) 014 3362, (555) 019 4408</div>
    </div>
    <div class="col-panel"></div>
    <div class="badge"><div class="badge-inner"><div class="badge-art ob" role="img" aria-label="Obstetrics and gynaecology emblem"></div></div></div>
    <div class="doctor">
      <div class="doctor-name">Dr. Arjun Mehra,</div>
      <div class="doctor-role">BMedSci, MBBS, DM (O&amp;G),<br>FACOG Obstetrician &amp; Gynaecologist</div>
    </div>
    <div class="email">
      <svg width="15" height="15" viewBox="0 0 16 16"><circle cx="8" cy="8" r="8" fill="#fff"/><rect x="4" y="5" width="8" height="6" fill="none" stroke="#e3242b" stroke-width="1.2"/><path d="M4 5l4 3.5L12 5" fill="none" stroke="#e3242b" stroke-width="1.2"/></svg>
      dr.mehra@mailbox.com
    </div>
    <div class="panel-rule"></div>
    <ul class="services services-group">
      <li><strong>Obstetrics:</strong>Prenatal Care, Delivery, Postnatal checks, High Risk pregnancy</li>
      <li><strong>Gynaecology :</strong>Pap smears, Abnormal vaginal bleeding, Fibroids, Colposcopy, Family planning, Infertility, Cancer screening, And More....</li>
    </ul>
  </section>

  <footer class="abs footer">
    <div class="abs address">
      <svg width="20" height="22" viewBox="0 0 20 22"><path d="M10 1a7 7 0 0 0-7 7c0 5 7 13 7 13s7-8 7-13a7 7 0 0 0-7-7z" fill="none" stroke="#e3242b" stroke-width="2"/><circle cx="10" cy="8" r="2.6" fill="#e3242b"/></svg>
      42 Harbour Road, Port Linden
    </div>
    <div class="abs footer-divider"></div>
    <div class="abs footer-phone">
      <svg width="24" height="24" viewBox="0 0 24 24"><circle cx="12" cy="12" r="11" fill="none" stroke="#e3242b" stroke-width="1.6"/><path d="M8 6.5l2 .3 1 3-1.4 1.2a8 8 0 0 0 3.4 3.4l1.2-1.4 3 1 .3 2c-.5 1-1.5 1.3-2.5 1.2A10 10 0 0 1 6.8 9c-.1-1 .2-2 1.2-2.5z" fill="#e3242b"/></svg>
      (555) 013 5520 / 5521
    </div>
  </footer>
</main>
</body>
</html>
```